We need a complete design for our construction company KELSO CONSTRUCTION based in Auckland New Zealand, we need a logo, website, business card, vehicle design etc..
We are a mid to high-end construction company who work mostly on residential projects and some commercial.

What we want to see in the design;
Professional,
Architectural,
Simple,
Alternative,

We want the design to communicate professionalism, high quality wormanship and and quality service.

Target Market(s)

People looking for a quality building/ construction company

Industry/Entity Type

Construction Company

Contact Information for Business Card

KELSO CONSTRUCTION.co.nz
Remi Tulvane
remi@kelsoconstruction-example.co.nz
021 5870 463

Logo Text

KELSO CONSTRUCTION

Number of Pages Required

5+ page

Font styles to use
Sans Serif

Colors

Designer to choose colors to be used in the design.

Requirements
Must have
• Must appear high end, professional, quality, be simple, easy to use, give security to potential clients
Nice to have
• high-quality photos of our recent projects
• about us page
• blog page
• contact us page
• high quality content
Should not have
• should not be hard to use and have too much going on.

```html
<!DOCTYPE html>
<html lang="en">
<head>
<meta charset="utf-8">
<title>Kelso Construction</title>
<link href="https://fonts.googleapis.com/css2?family=Poppins:wght@400;500;600&family=Open+Sans:ital,wght@0,400;0,600;1,600&display=swap" rel="stylesheet">
<style>
:root{
  --gold:#e7b01b;
  --blue:#2e9fd9;
  --blue-dark:#2583b8;
  --navy:#2b3b4e;
  --ink:#1c1c1c;
  --body:#555;
  --sky:#eef8fd;
  --white:#fff;
}
*{margin:0;padding:0;box-sizing:border-box}
html,body{width:1200px;height:3681px;overflow:hidden}
body{position:relative;background:var(--white);font-family:"Open Sans",sans-serif;color:var(--body)}
.abs{position:absolute}
h2{font-family:"Poppins",sans-serif;font-weight:500;font-size:38px;color:var(--ink);text-align:center;position:absolute;left:0;width:1200px}
h2 span{color:var(--gold)}
.lead{position:absolute;left:150px;width:900px;text-align:center;font-size:14px;line-height:24px;color:var(--body)}
.btn{position:absolute;background:var(--gold);color:var(--ink);font-family:"Poppins",sans-serif;font-weight:500;font-size:15px;display:flex;align-items:center;justify-content:center}

/* header */
.topbar{left:490px;top:0;width:710px;height:50px;background:var(--gold);clip-path:polygon(0 0,100% 0,100% 100%,60px 100%)}
.contact-line{top:14px;right:100px;color:#fff;font-size:14px;display:flex;gap:36px}
.contact-line span{display:flex;align-items:center;gap:8px}
.brand{left:108px;top:26px;display:flex;align-items:center;gap:12px}
.brand-mark{width:46px;height:46px;border:4px solid var(--blue)}
.brand-name{font-family:"Poppins",sans-serif;font-size:30px;color:var(--blue);line-height:1;font-weight:400}
.nav{top:76px;right:100px;display:flex;gap:40px;font-family:"Poppins",sans-serif;font-size:16px;color:var(--ink)}

/* hero */
.hero{left:0;top:128px;width:1200px;height:504px;background:linear-gradient(135deg,#1f2f44 0%,#4f6478 45%,#c9bda6 75%,#2c3b50 100%)}
.hero-sub{top:308px;left:0;width:1200px;text-align:center;font-family:"Poppins",sans-serif;font-size:30px;color:#fff}
.hero-title{top:362px;left:0;width:1200px;text-align:center;font-family:"Poppins",sans-serif;font-weight:600;font-size:50px;color:#fff;letter-spacing:1px}

/* about */
.about-photo{left:108px;top:974px;width:437px;height:297px;background:linear-gradient(135deg,#8a6a4c,#c9b79c 50%,#5c6470)}
.about-col{left:594px;top:966px;width:500px}
.about-col h3{font-family:"Poppins",sans-serif;font-weight:500;font-size:21px;color:var(--blue)}
.about-col p{font-size:14px;line-height:24px;margin-top:12px}
.features{left:594px;top:1096px;width:520px;display:grid;grid-template-columns:295px 225px;row-gap:14px;font-family:"Poppins",sans-serif;font-size:15px;font-weight:500;color:var(--ink)}
.features div{display:flex;align-items:center;gap:10px}
.features i{width:14px;height:14px;background:var(--gold);display:inline-block;border-radius:3px}

/* services */
.services{left:0;top:1357px;width:1200px;height:515px;background:var(--sky)}
.service{position:absolute;top:1576px;width:240px;text-align:center}
.service .ring{width:112px;height:112px;border-radius:50%;border:3px solid var(--gold);background:#fff7dc;margin:0 auto;display:flex;align-items:center;justify-content:center}
.service h4{font-family:"Poppins",sans-serif;font-weight:500;font-size:19px;color:var(--ink);margin-top:28px}
.service p{font-size:14px;line-height:22px;margin-top:8px}

/* process */
.process{left:0;top:1872px;width:1200px;height:550px;background:linear-gradient(180deg,#3a4a5e,#2b3b4e 60%,#26364a)}
.worker-photo{left:98px;top:1835px;width:270px;height:587px;background:linear-gradient(180deg,#4a5d78 0%,#3e5474 50%,#33465f 100%)}
.process-title{position:absolute;left:447px;top:1940px;font-family:"Poppins",sans-serif;font-weight:500;font-size:38px;color:#fff}
.step{position:absolute;left:447px;width:595px;display:flex;align-items:flex-start;border-bottom:1px solid rgba(255,255,255,.35)}
.step b{font-family:"Poppins",sans-serif;font-weight:600;font-size:54px;color:#fff;width:86px;line-height:1}
.step h5{font-family:"Poppins",sans-serif;font-weight:500;font-size:21px;color:#fff;margin-top:8px}
.step p{font-size:13px;line-height:20px;color:#dfe5ea;width:440px}
.step svg{margin-left:auto}

/* projects */
.side-shot{top:2636px;height:365px;background:linear-gradient(180deg,#cfe3ef,#9fb58a)}
.main-shot{left:236px;top:2636px;width:728px;height:365px;background:linear-gradient(180deg,#bcd7ec 0%,#d8d3c8 50%,#6f9a3c 100%)}
.proj-card{left:798px;top:2675px;width:319px;height:285px;background:#f1f1f1;padding:34px 30px}
.proj-card h4{font-family:"Poppins",sans-serif;font-weight:500;font-size:23px;line-height:26px;color:var(--ink)}
.proj-card p{font-size:13px;line-height:21px;margin-top:14px}
.sq-arrow{top:2955px;width:38px;height:38px;background:var(--blue);display:flex;align-items:center;justify-content:center}

/* testimonial */
.quote{left:240px;top:3166px;width:720px;text-align:center;font-style:italic;font-weight:600;font-size:13px;line-height:24px;color:#333}
.author{left:800px;top:3236px;width:160px;text-align:right;font-family:"Poppins",sans-serif;font-size:18px;color:var(--blue)}

/* footer */
.footer{left:0;top:3352px;width:1200px;height:255px;background:var(--blue)}
.copy{left:0;top:3607px;width:1200px;height:74px;background:var(--blue-dark);color:#fff;font-size:13px;display:flex;align-items:center;justify-content:center}
.f-brand{left:178px;top:3412px;display:flex;align-items:center;gap:12px}
.f-brand .brand-mark{border-color:#fff}
.f-brand .brand-name{color:#fff}
.socials{left:172px;top:3500px;display:flex;gap:10px}
.socials i{width:42px;height:42px;border-radius:6px;display:block}
.f-head{font-family:"Poppins",sans-serif;font-weight:500;font-size:19px;color:#fff}
.links{left:530px;top:3452px;list-style:none;font-size:13px;color:#fff;line-height:25px}
.field{position:absolute;left:697px;width:345px;border-bottom:1px solid #fff;color:#fff;font-size:13px;padding-bottom:8px}
</style>
</head>
<body>

<!-- header -->
<div class="abs topbar"></div>
<div class="abs contact-line">
  <span><svg width="13" height="13" viewBox="0 0 24 24"><path fill="#fff" d="M6.6 10.8a15 15 0 006.6 6.6l2.2-2.2a1 1 0 011-.2 11 11 0 003.6.6 1 1 0 011 1V20a1 1 0 01-1 1A17 17 0 013 4a1 1 0 011-1h3.5a1 1 0 011 1 11 11 0 00.6 3.6 1 1 0 01-.3 1z"/></svg>+64 9 555 0142</span>
  <span><svg width="14" height="12" viewBox="0 0 24 20"><rect x="1" y="1" width="22" height="18" fill="none" stroke="#fff" stroke-width="2"/><path d="M1 2l11 9 11-9" fill="none" stroke="#fff" stroke-width="2"/></svg>info@kelsoconstruction-example.co.nz</span>
</div>
<div class="abs brand"><div class="brand-mark"></div><div class="brand-name">KELSO<br>Construction</div></div>
<nav class="abs nav"><span>HOME</span><span>ABOUT US</span><span>PROJECTS</span><span>BLOG</span><span>CONTACT US</span></nav>

<!-- hero -->
<div class="abs hero" role="img" aria-label="Two architects studying a scale model of a building"></div>
<svg class="abs" style="left:0;top:600px" width="1200" height="150" viewBox="0 0 1200 150">
  <polygon points="0,32 390,32 600,140 810,32 1200,32 1200,150 0,150" fill="#fff"/>
  <polygon points="390,32 600,140 810,32 600,110" fill="var(--blue)"/>
  <polygon points="0,0 600,30 1200,0 1200,32 810,32 600,110 390,32 0,32" fill="#fff"/>
</svg>
<div class="abs hero-sub">Kelso Construction</div>
<div class="abs hero-title">YOU DREAM, WE CREATE</div>
<svg class="abs" style="left:0;top:362px" width="30" height="60"><rect width="30" height="60" fill="rgba(0,0,0,.35)"/><path d="M20 18L10 30l10 12" stroke="#fff" stroke-width="4" fill="none"/></svg>
<svg class="abs" style="left:1170px;top:362px" width="30" height="60"><rect width="30" height="60" fill="rgba(0,0,0,.35)"/><path d="M10 18l10 12-10 12" stroke="#fff" stroke-width="4" fill="none"/></svg>

<!-- about -->
<h2 style="top:818px">About <span>Us</span></h2>
<p class="lead" style="top:884px">Lorem ipsum dolor sit amet, consectetur adipiscing elit, sed do eiusmod tempor incididunt ut labore et dolore magna aliqua. Ut enim ad minim veniam, quis nostrud exercitation ullamco laboris nisi ut aliquip ex ea commodo consequat.</p>
<div class="abs about-photo" role="img" aria-label="Builders in hard hats reviewing plans on site"></div>
<div class="abs about-col">
  <h3>We Offer Best Services &amp; Solutions:</h3>
  <p>Sed ut perspiciatis unde omnis iste natus error sit voluptatem accusantium do loremque laudantium, totam rem aperiam, eaque ipsa quae ab illo inventore veritatis et quasi architecto beatae vitae dicta sunt explicabo.</p>
</div>
<div class="abs features">
  <div><i></i>Expert &amp; Professional</div><div><i></i>Satisfaction Guarantee</div>
  <div><i></i>Professional Approach</div><div><i></i>Quick In Response</div>
  <div><i></i>High Quality Work</div><div><i></i>24/7 Emergency</div>
</div>
<div class="btn" style="left:594px;top:1225px;width:125px;height:34px">Read More</div>

<!-- services -->
<div class="abs services"></div>
<h2 style="top:1428px">Our <span>Services</span></h2>
<p class="lead" style="top:1500px">Lorem ipsum dolor sit amet, consectetur adipiscing elit, sed do eiusmod tempor incididunt ut labore et dolore magna aliqua. Ut enim ad minim veniam, quis nostrud exercitation ullamco laboris nisi ut aliquip ex ea commodo consequat.</p>
<div class="service" style="left:91px"><div class="ring"><svg width="50" height="50" viewBox="0 0 50 50" fill="none" stroke="var(--blue)" stroke-width="2.5"><circle cx="25" cy="9" r="4"/><path d="M23 13L12 44M27 13l11 31M15 32h20"/></svg></div><h4>Architectural Design</h4><p>Sed ut perspiciatis unde omnis iste natus error sit voluptate ium.</p></div>
<div class="service" style="left:346px"><div class="ring"><svg width="50" height="50" viewBox="0 0 50 50" fill="none" stroke="var(--blue)" stroke-width="2.5"><path d="M10 40L36 14M32 10a7 7 0 008 8M40 40L14 14M10 10l4 4"/></svg></div><h4>Renovation Services</h4><p>Sed ut perspiciatis unde omnis iste natus error sit voluptate ium.</p></div>
<div class="service" style="left:604px"><div class="ring"><svg width="50" height="50" viewBox="0 0 50 50" fill="none" stroke="var(--blue)" stroke-width="2.5"><path d="M18 8v10M32 8v10M14 18h22v8a11 11 0 01-22 0zM25 37v8"/></svg></div><h4>Electrical System</h4><p>Sed ut perspiciatis unde omnis iste natus error sit voluptate ium.</p></div>
<div class="service" style="left:862px"><div class="ring"><svg width="50" height="50" viewBox="0 0 50 50" fill="none" stroke="var(--blue)" stroke-width="2.5"><path d="M12 14h26l6 22H6zM9 25h32M19 14l-3 22M31 14l3 22M25 14v22"/></svg></div><h4>Roofing</h4><p>Sed ut perspiciatis unde omnis iste natus error sit voluptate ium.</p></div>

<!-- process -->
<div class="abs process" role="img" aria-label="Evening city skyline in muted blue tones"></div>
<div class="abs worker-photo" role="img" aria-label="Smiling builder in a hard hat and tool belt"></div>
<h3 class="process-title">Process We Follow</h3>
<div class="step" style="top:2010px;height:95px"><b>01</b><div><h5>Project Initiation</h5><p>Lorem ipsum dolor sit amet, consectetur adipiscing elit, sed do eiusmod tempor incididunt ut labore et dolore magna aliqua ut enim ad.</p></div><svg width="60" height="60" viewBox="0 0 60 60" fill="none" stroke="var(--gold)" stroke-width="2.5"><path d="M8 40l30-30 12 12-30 30zM14 46l-6 6M30 18l8 8"/></svg></div>
<div class="step" style="top:2118px;height:80px"><b>02</b><h5>Achitect Selection</h5><svg width="60" height="60" viewBox="0 0 60 60" fill="none" stroke="var(--gold)" stroke-width="2.5"><path d="M18 22a12 12 0 0124 0zM14 24h32M22 30a8 8 0 0016 0M16 56v-8a14 14 0 0128 0v8"/></svg></div>
<div class="step" style="top:2210px;height:80px"><b>03</b><h5>Building Programs</h5><svg width="60" height="60" viewBox="0 0 60 60" fill="none" stroke="var(--gold)" stroke-width="2.5"><path d="M10 50L44 16M40 10a8 8 0 009 9M50 50L18 18M12 12l6 6"/></svg></div>
<div class="step" style="top:2302px;height:80px;border-bottom:none"><b>04</b><h5>Finalize Construction</h5><svg width="70" height="60" viewBox="0 0 70 60" fill="none" stroke="var(--gold)" stroke-width="2.5"><path d="M6 26L35 8l29 18M12 22v30h46V22M4 52h62M20 34h8v8h-8zM42 34h8v8h-8zM31 40h8v12h-8z"/></svg></div>

<!-- projects -->
<h2 style="top:2492px">Recent <span>Projects</span></h2>
<p class="lead" style="top:2552px;left:320px;width:560px">Lorem Ipsum is simply dummy text of the printing and typesetting industry. Lorem Ipsum has been the industry's standard dummy text ever since the 1500s.</p>
<div class="abs side-shot" style="left:0;width:113px" role="img" aria-label="Palm-lined residential project"></div>
<div class="abs main-shot" role="img" aria-label="Modern two-storey home with pool and lawn"></div>
<div class="abs side-shot" style="left:1085px;width:115px" role="img" aria-label="Residential project with trees"></div>
<div class="abs proj-card"><h4>Building Construction Project</h4><p>Sed ut perspiciatis unde omnis iste natus error sit voluptatem accusantium doloremque laudantium, tatis et quasi arvitae dicta sunt explicabo.</p></div>
<div class="btn" style="left:828px;top:2878px;width:125px;height:34px">Read More</div>
<div class="abs sq-arrow" style="left:241px"><svg width="14" height="18"><path d="M11 2L4 9l7 7" stroke="#fff" stroke-width="3" fill="none"/></svg></div>
<div class="abs sq-arrow" style="left:290px"><svg width="14" height="18"><path d="M3 2l7 7-7 7" stroke="#fff" stroke-width="3" fill="none"/></svg></div>

<!-- testimonial -->
<h2 style="top:3080px">Client's <span>Words</span></h2>
<svg class="abs" style="left:98px;top:3180px" width="24" height="38"><path d="M20 3L5 19l15 16" stroke="#aaa" stroke-width="3" fill="none"/></svg>
<svg class="abs" style="left:1076px;top:3180px" width="24" height="38"><path d="M4 3l15 16L4 35" stroke="#aaa" stroke-width="3" fill="none"/></svg>
<p class="abs quote">Nam libero tempore, cum soluta nobis est eligendi optio cumque nihil impedit quo minus id quod maxime placeat facere possimus, omnis voluptas assumenda est, omnis dolor repellendus. Temporibus autem quibusdam et aut officiis debitis aut rerum necessitatibus saepe eveniet ut et voluptates repudiandae sint et molestiae non recusandae.</p>
<div class="abs author">– Marlow</div>
<svg class="abs" style="left:880px;top:3266px" width="80" height="16" viewBox="0 0 80 16"><g fill="var(--gold)"><path id="st" d="M8 0l2.4 5 5.6.6-4.2 3.8 1.2 5.6L8 12.2 3 15l1.2-5.6L0 5.6 5.6 5z"/><use href="#st" x="16"/><use href="#st" x="32"/><use href="#st" x="48"/><use href="#st" x="64"/></g></svg>

<!-- footer -->
<div class="abs footer"></div>
<div class="abs f-brand"><div class="brand-mark"></div><div class="brand-name">KELSO<br>Construction</div></div>
<div class="abs socials"><i style="background:#55acee"></i><i style="background:#3b5998"></i><i style="background:#dd4b39"></i><i style="background:#e52d27"></i></div>
<div class="abs f-head" style="left:530px;top:3400px">Links</div>
<ul class="abs links"><li>Home</li><li>About us</li><li>Projects</li><li>Blog</li><li>Contact us</li></ul>
<div class="abs f-head" style="left:697px;top:3400px">Get In touch</div>
<div class="field" style="top:3454px">Name</div>
<div class="field" style="top:3497px">Email</div>
<div class="btn" style="left:942px;top:3544px;width:100px;height:34px">Submit</div>
<div class="abs copy">Copyright © 2018. All Rights Reserved.</div>

</body>
</html>
```